Before & After School Care Business - Service Promotional Flyer

Need service promotional flyer for when parents (customers) are enrolling kids in school for first time. This flyer is specifically aimed at parents with kids aged 4 - 7 years old and needs to communicate crazy, fun and energy. We have five programs which we operate every school daily all based within local school halls. The flyer will be added to the local schools welcome to school pack. We also run School Holiday Programs supporting busy working families.

Industry/Entity Type

Business

```html
<!DOCTYPE html>
<html lang="en">
<head>
<meta charset="utf-8">
<title>Play Burst – Welcome to School Flyer</title>
<link href="https://fonts.googleapis.com/css2?family=Oswald:wght@600;700&family=Comic+Neue:wght@700&family=Open+Sans:ital,wght@0,400;1,700&family=Roboto+Condensed:wght@700&display=swap" rel="stylesheet">
<style>
  :root{
    --pink:#e5127d;
    --yellow:#ffc20e;
    --blue:#1ba1e2;
    --ink:#2b2b2b;
    --white:#ffffff;
  }
  *{margin:0;padding:0;box-sizing:border-box;}
  html,body{width:907px;height:1200px;overflow:hidden;background:var(--white);}
  .flyer{position:relative;width:907px;height:1200px;overflow:hidden;background:var(--white);}
  .flyer-art{position:absolute;inset:0;}
  .brand{position:absolute;left:92px;top:660px;display:flex;align-items:center;gap:14px;}
  .brand-dot{width:40px;height:40px;border-radius:50%;background:var(--blue);}
  .brand-name{font-family:'Oswald',sans-serif;font-weight:700;font-size:44px;color:var(--pink);letter-spacing:1px;}
  .headline{position:absolute;left:58px;top:790px;font-family:'Oswald',sans-serif;font-weight:700;font-size:56px;line-height:1;color:var(--pink);letter-spacing:.5px;}
  .subhead{position:absolute;left:60px;top:855px;font-family:'Comic Neue',sans-serif;font-weight:700;font-size:38px;color:var(--ink);}
  .holiday-pill{position:absolute;left:0;top:912px;width:520px;height:82px;background:var(--blue);border-radius:0 41px 41px 0;padding:10px 0 0 60px;font-family:'Open Sans',sans-serif;font-style:italic;font-weight:700;font-size:22px;line-height:30px;color:var(--white);}
  .phone{position:absolute;left:60px;top:1005px;font-family:'Roboto Condensed',sans-serif;font-weight:700;font-size:64px;color:var(--ink);letter-spacing:1px;}
  .contact{position:absolute;font-family:'Open Sans',sans-serif;font-size:18px;line-height:24px;color:var(--white);display:flex;gap:8px;}
  .contact svg{flex:none;margin-top:3px;}
  .contact-address{left:60px;top:1128px;}
  .contact-online{left:340px;top:1120px;flex-direction:column;gap:4px;}
  .contact-line{display:flex;gap:8px;align-items:center;}
</style>
</head>
<body>
<main class="flyer">
  <svg class="flyer-art" width="907" height="1200" viewBox="0 0 907 1200">
    <defs>
      <linearGradient id="grey-fade" x1="0" y1="0" x2="0" y2="1">
        <stop offset="0" stop-color="#d9d9d9"/><stop offset="1" stop-color="#f4f4f4"/>
      </linearGradient>
      <radialGradient id="huddle-tones" cx=".5" cy=".5" r=".6">
        <stop offset="0" stop-color="#cfe6f5"/><stop offset=".55" stop-color="#e8b79a"/><stop offset="1" stop-color="#6fae4a"/>
      </radialGradient>
      <linearGradient id="playground-tones" x1="0" y1="0" x2="0" y2="1">
        <stop offset="0" stop-color="#a9cbe8"/><stop offset="1" stop-color="#8b8c8f"/>
      </linearGradient>
      <linearGradient id="splash-tones" x1="0" y1="0" x2="1" y2="1">
        <stop offset="0" stop-color="#e9b69a"/><stop offset="1" stop-color="#8a5a45"/>
      </linearGradient>
    </defs>

    <rect class="faded-backdrop" x="640" y="0" width="267" height="330" fill="url(#grey-fade)" role="img" aria-label="Faded photo of children at school"/>

    <path class="swoosh-blue" d="M0,520 C220,650 520,700 907,610 L907,640 C540,760 200,705 0,612 Z" fill="var(--blue)"/>

    <circle cx="430" cy="225" r="306" fill="none" stroke="var(--yellow)" stroke-width="16"/>
    <circle cx="430" cy="225" r="290" fill="none" stroke="var(--pink)" stroke-width="16"/>
    <circle cx="430" cy="225" r="282" fill="url(#huddle-tones)" role="img" aria-label="Photo of smiling children huddled together looking down at the camera"/>

    <g class="photo-bubble">
      <circle cx="685" cy="435" r="132" fill="var(--yellow)"/>
      <circle cx="685" cy="435" r="122" fill="var(--pink)"/>
      <circle cx="685" cy="435" r="113" fill="url(#playground-tones)" role="img" aria-label="Photo of children playing in the school playground"/>
    </g>
    <g class="photo-bubble">
      <circle cx="518" cy="585" r="100" fill="var(--yellow)"/>
      <circle cx="518" cy="585" r="91" fill="var(--pink)"/>
      <circle cx="518" cy="585" r="83" fill="url(#playground-tones)" role="img" aria-label="Photo of a child hanging upside down on play equipment"/>
    </g>
    <g class="photo-bubble">
      <circle cx="716" cy="632" r="80" fill="var(--yellow)"/>
      <circle cx="716" cy="632" r="72" fill="var(--pink)"/>
      <circle cx="716" cy="632" r="65" fill="url(#playground-tones)" role="img" aria-label="Photo of a child climbing on a playground frame"/>
    </g>

    <path class="swoosh-yellow" d="M0,1085 C300,1120 600,1100 907,1030" fill="none" stroke="var(--yellow)" stroke-width="10"/>
    <path class="swoosh-pink" d="M0,1070 C300,1105 600,1085 907,1012" fill="none" stroke="var(--pink)" stroke-width="8"/>
    <path class="footer-band" d="M0,1100 C300,1135 600,1115 907,1048 L907,1200 L0,1200 Z" fill="var(--blue)"/>

    <path class="splash-photo" d="M600,1200 L600,900 C600,820 640,770 700,760 L820,760 C880,770 907,820 907,860 L907,1200 Z" fill="url(#splash-tones)" role="img" aria-label="Photo of two children cheering with arms raised at the pool"/>
  </svg>

  <div class="brand">
    <span class="brand-dot"></span>
    <span class="brand-name">PLAY BURST</span>
  </div>

  <h1 class="headline">THE LOCAL SCHOOLS</h1>
  <p class="subhead">welcome to school pack</p>

  <p class="holiday-pill">We also run School Holiday Programs<br>supporting busy working families</p>

  <p class="phone">0800 321 4870</p>

  <div class="contact contact-address">
    <svg width="14" height="18" viewBox="0 0 14 18"><path d="M7 0a7 7 0 0 0-7 7c0 5 7 11 7 11s7-6 7-11a7 7 0 0 0-7-7zm0 9.5A2.5 2.5 0 1 1 7 4.5a2.5 2.5 0 0 1 0 5z" fill="var(--yellow)"/></svg>
    <span>PO Box 18, Ridgefield<br>New Zealand</span>
  </div>

  <div class="contact contact-online">
    <span class="contact-line">
      <svg width="18" height="13" viewBox="0 0 18 13"><rect x="1" y="1" width="16" height="11" fill="none" stroke="var(--yellow)" stroke-width="1.6"/><path d="M1 1l8 6 8-6" fill="none" stroke="var(--yellow)" stroke-width="1.6"/></svg>
      hello@playburst.co.nz
    </span>
    <span class="contact-line">
      <svg width="18" height="18" viewBox="0 0 18 18"><circle cx="9" cy="9" r="7.5" fill="none" stroke="var(--yellow)" stroke-width="1.6"/><path d="M1.5 9h15M9 1.5c3 3.5 3 11.5 0 15M9 1.5c-3 3.5-3 11.5 0 15" fill="none" stroke="var(--yellow)" stroke-width="1.3"/></svg>
      www.playburst.co.nz
    </span>
  </div>
</main>
</body>
</html>
```